Australia's newest tech recruitment startup

We are a new tech startup in the recruitment space.

We leverage the existing infrastructure of the recruitment network and bundle a value market based business model (like brisk fennel) that appeals to business.

We are very individual, afraid of no one, minimalist, and defiantly NO "BS"!!

We're not cut price think Vantor Hale rather than Kesumi
Updates

Hey Everyone,

thanks so much for your designs. I have eliminated a lot of designs but if I havent to yours then your in with a shot. I would like to see the designs updated with a spot for our twitter handle, my blog address & our linkedIn group address. 

For some designs I think some of the above would look ok on the back of the card so not to make the front look too messy. 

thanks   

Target Market(s)

Our target market is SME's young baby boomer and Gen X

Industry/Entity Type

Business

Requirements
Must have
• Company logo, doesn't have to be both

```html
<!DOCTYPE html>
<html lang="en">
<head>
<meta charset="utf-8">
<title>BrightRoster — Business Card</title>
<link rel="stylesheet" href="https://fonts.googleapis.com/css2?family=Play:wght@400;700&display=swap">
<style>
  :root {
    --stage: #e9ebee;
    --card: #f5f8fc;
    --card-edge: #e6eef8;
    --ink: #3b404a;
    --ink-soft: #4f5560;
    --accent: #5d82c4;
    --brand: #6badde;
  }
  * { box-sizing: border-box; margin: 0; padding: 0; }
  html, body {
    width: 1200px;
    height: 750px;
    overflow: hidden;
    background: var(--stage);
    font-family: "Play", "Trebuchet MS", sans-serif;
    color: var(--ink);
  }
  .stage { position: relative; width: 1200px; height: 750px; }

  .card {
    position: absolute;
    width: 600px;
    height: 346px;
    background: radial-gradient(ellipse at center, #fbfcfe 0%, var(--card) 60%, var(--card-edge) 100%);
    box-shadow: 0 1px 3px rgba(0,0,0,0.12);
  }
  .card--back { left: 504px; top: 84px; }
  .card--front { left: 103px; top: 326px; display: flex; align-items: center; justify-content: center; }

  .identity {
    position: absolute;
    right: 366px;
    top: 128px;
    text-align: right;
  }
  .identity__name {
    font-size: 21px;
    color: var(--ink);
    padding: 0 0 3px 0;
    border-bottom: 2px solid var(--accent);
    letter-spacing: 0.2px;
  }
  .identity__role {
    font-size: 17px;
    color: var(--ink-soft);
    margin-top: 5px;
  }

  .divider {
    position: absolute;
    left: 255px;
    top: 81px;
    width: 2px;
    height: 166px;
    background: linear-gradient(to bottom, rgba(93,130,196,0), var(--accent) 20%, var(--accent) 80%, rgba(93,130,196,0));
  }

  .contact {
    position: absolute;
    left: 270px;
    top: 107px;
    list-style: none;
    font-size: 17px;
    line-height: 24px;
    color: var(--ink-soft);
  }
  .contact__item { display: flex; align-items: flex-start; }
  .contact__icon { width: 20px; height: 24px; margin-right: 8px; flex: none; }
  .contact__indent { padding-left: 28px; }
  .contact__at { color: var(--accent); }

  .brand-name {
    font-size: 58px;
    font-weight: 700;
    color: var(--brand);
    letter-spacing: -0.5px;
    margin-top: 6px;
  }
</style>
</head>
<body>
<main class="stage">
  <section class="card card--back" aria-label="Card back">
    <div class="identity">
      <p class="identity__name">Reid Calloway</p>
      <p class="identity__role">Director</p>
    </div>
    <div class="divider"></div>
    <ul class="contact">
      <li class="contact__item">
        <svg class="contact__icon" viewBox="0 0 20 24" aria-hidden="true">
          <circle cx="9" cy="12" r="7" fill="none" stroke="#5d82c4" stroke-width="2"/>
          <circle cx="9" cy="12" r="3" fill="#5d82c4"/>
        </svg>
        <span>18 Harbour Lane Westvale</span>
      </li>
      <li class="contact__item contact__indent">Northgate</li>
      <li class="contact__item">
        <svg class="contact__icon" viewBox="0 0 20 24" aria-hidden="true">
          <rect x="4" y="6" width="9" height="15" rx="1.5" fill="none" stroke="#5d82c4" stroke-width="1.6"/>
          <line x1="6" y1="2" x2="6" y2="6" stroke="#5d82c4" stroke-width="1.6"/>
          <rect x="6" y="8.5" width="5" height="4" fill="#5d82c4" opacity="0.6"/>
        </svg>
        <span>104-555-0187</span>
      </li>
      <li class="contact__item">
        <svg class="contact__icon" viewBox="0 0 20 24" aria-hidden="true">
          <rect x="1.5" y="6" width="15" height="11" fill="#8fb0dc" stroke="#5d82c4" stroke-width="1.4"/>
          <line x1="9" y1="17" x2="9" y2="20" stroke="#5d82c4" stroke-width="1.6"/>
          <line x1="5" y1="21" x2="13" y2="21" stroke="#5d82c4" stroke-width="1.6"/>
        </svg>
        <span>info<span class="contact__at">@</span>brightroster.com</span>
      </li>
    </ul>
  </section>

  <section class="card card--front" aria-label="Card front">
    <p class="brand-name">BrightRoster</p>
  </section>
</main>
</body>
</html>
```